KORBALT

The business want a professional looking business card. We have a scetch we will add but want the extra upgrade, and would like more suggestions for variations of our business cards.

```html
<!DOCTYPE html>
<html lang="en">
<head>
<meta charset="utf-8">
<title>KORBALT – Business Card</title>
<link rel="stylesheet" href="https://fonts.googleapis.com/css2?family=Cinzel:wght@400;500;600&family=Oswald:wght@500&family=Montserrat:wght@300;600&family=PT+Serif&display=swap">
<style>
  :root {
    --canvas-bg: #ecebe8;
    --gold-light: #ead0a0;
    --gold-mid: #c9a673;
    --gold-face-start: #94773f;
    --gold-face-mid: #7e6138;
    --gold-face-end: #4a2120;
    --ink-black: #0b0b0d;
    --wordmark: #b8905e;
    --cream-text: #f3e6cf;
    --muted-text: #e2cfb3;
  }
  * { box-sizing: border-box; margin: 0; padding: 0; }
  html, body { width: 1200px; height: 1047px; overflow: hidden; }
  body {
    background: var(--canvas-bg);
    display: flex;
    align-items: center;
    justify-content: center;
    gap: 30px;
  }
  .card {
    position: relative;
    width: 570px;
    height: 326px;
    overflow: hidden;
    box-shadow: 0 4px 14px rgba(0,0,0,0.18);
  }
  /* Front */
  .card--front {
    background: linear-gradient(90deg, var(--gold-face-start) 0%, var(--gold-face-mid) 55%, var(--gold-face-end) 100%);
  }
  .ornament-area {
    position: absolute;
  }
  .card--front .ornament-area--left {
    left: 0; top: 0; width: 170px; height: 326px;
    background: radial-gradient(ellipse at 20% 50%, rgba(240,215,170,0.55) 0%, rgba(240,215,170,0.18) 45%, rgba(240,215,170,0) 75%);
  }
  .card--front .ornament-area--cluster {
    left: 410px; top: 145px; width: 140px; height: 140px;
    background: radial-gradient(circle, rgba(240,215,170,0.45) 0%, rgba(240,215,170,0.15) 50%, rgba(240,215,170,0) 72%);
  }
  .company-name {
    position: absolute;
    right: 20px; top: 22px;
    font-family: "Oswald", sans-serif;
    font-weight: 500;
    font-size: 28px;
    letter-spacing: 0.02em;
    color: var(--gold-light);
  }
  .person-name {
    position: absolute;
    right: 20px; top: 72px;
    font-family: "Cinzel", serif;
    font-weight: 500;
    font-size: 19px;
    color: var(--cream-text);
  }
  .person-role {
    position: absolute;
    right: 20px; top: 101px;
    font-family: "Montserrat", sans-serif;
    font-weight: 300;
    font-size: 11.5px;
    letter-spacing: 0.06em;
    color: var(--muted-text);
  }
  .contact-line {
    position: absolute;
    right: 20px; bottom: 18px;
    display: flex;
    gap: 22px;
    font-family: "PT Serif", serif;
    font-size: 10.5px;
    color: var(--cream-text);
  }
  /* Back */
  .card--back { background: var(--ink-black); }
  .card--back .ornament-area--left {
    left: 0; top: 60px; width: 95px; height: 210px;
    background: radial-gradient(ellipse at 20% 50%, rgba(110,100,90,0.45) 0%, rgba(110,100,90,0) 70%);
  }
  .card--back .ornament-area--right {
    right: 0; top: 60px; width: 95px; height: 210px;
    background: radial-gradient(ellipse at 80% 50%, rgba(110,100,90,0.45) 0%, rgba(110,100,90,0) 70%);
  }
  .wordmark {
    position: absolute;
    left: 0; right: 0; top: 122px;
    text-align: center;
    font-family: "Cinzel", serif;
    font-weight: 500;
    font-size: 44px;
    letter-spacing: 0.24em;
    padding-left: 0.24em;
    color: var(--wordmark);
  }
  .tagline {
    position: absolute;
    left: 0; right: 0; top: 190px;
    text-align: center;
    font-family: "Montserrat", sans-serif;
    font-weight: 600;
    font-size: 15px;
    letter-spacing: 0.38em;
    padding-left: 0.38em;
    color: var(--gold-mid);
  }
</style>
</head>
<body>
  <section class="card card--front">
    <div class="ornament-area ornament-area--left" role="img" aria-label="Decorative gold ornament along left edge"></div>
    <div class="ornament-area ornament-area--cluster" role="img" aria-label="Decorative gold ornament cluster"></div>
    <h1 class="company-name">KORBALT SOLVANG</h1>
    <p class="person-name">Lars Henrik Solvang</p>
    <p class="person-role">CEO &amp; FOUNDER</p>
    <p class="contact-line">
      <span class="contact-phone">004791 550274</span>
      <span class="contact-email">korbalt.llc@mailbox.com</span>
      <span class="contact-web">www.korbalt.llc</span>
    </p>
  </section>

  <section class="card card--back">
    <div class="ornament-area ornament-area--left" role="img" aria-label="Faint decorative ornament at left edge"></div>
    <div class="ornament-area ornament-area--right" role="img" aria-label="Faint decorative ornament at right edge"></div>
    <h2 class="wordmark">KORBALT</h2>
    <p class="tagline">SINCE 2026</p>
  </section>
</body>
</html>
```